stars + comments Reviews website design (similar to grubly concept)

Please refer to attached logo and wire frames
----------------------------------------------------------------------------------------------------
we are a company based in egypt, seeking a design for a website that allows user to find doctors using search and filters.
also it allows user to review this doctor through providing comment and 1 to 5 stars
i need 4 main pages designs:
1- Doctors list/favorites list
2- Doctor view
3- Add doctor (3 steps)
4- Sign-in/sign up
5- Menu design
am into the colors teal/turquoise (though am open for different opinion)
i don't want the design theme to be doctors specific
am into the school of very clean, very neat, very simple
(chirpnet, pagecircle, snapmosaic designs are appealing to me)
Updates

Number of Pages Required

4 page

Font styles to use
Sans Serif

Colors
00a990
33b8a4

Requirements
Must have
• website will be bilingual/ bi-directional (English and Arabic)
• designer needs to provide another copy of the design with "right to left" orientation
• interactive button animation

```html
<!DOCTYPE html>
<html lang="en">
<head>
<meta charset="utf-8">
<title>Curanota – Reviewed Doctors</title>
<link href="https://fonts.googleapis.com/css2?family=Lato:wght@400;700;900&display=swap" rel="stylesheet">
<style>
:root{
  --teal:#00a990;
  --teal-dark:#0a8f86;
  --teal-deep:#0b5f5a;
  --teal-light:#33b8a4;
  --page:#f0f0f0;
  --card:#ffffff;
  --ink:#3a3a3a;
  --ink-soft:#555;
  --muted:#9a9a9a;
  --star-off:#b5b5b5;
  --footer:#363636;
  --footer-base:#262626;
  --footer-text:#b8b8b8;
}
*{box-sizing:border-box;margin:0;padding:0}
html,body{width:1136px;height:1200px;overflow:hidden}
body{font-family:'Lato',sans-serif;background:var(--page);color:var(--ink);position:relative}

.site-header{position:absolute;left:0;top:0;width:1136px;height:138px;
  background:linear-gradient(110deg,#0b9a98 0%,#13a9a6 40%,#0c9592 70%,#0e8f8c 100%);}
.brand{position:absolute;left:94px;top:22px;display:flex;align-items:center;gap:10px;color:#fff;
  font-weight:900;font-size:40px;letter-spacing:-0.5px}
.brand-dot{width:18px;height:18px;border-radius:50%;background:#fff}
.main-nav{position:absolute;left:352px;top:50px;display:flex;align-items:center;gap:0;
  font-size:12px;color:#fff;text-transform:uppercase}
.main-nav a{color:#fff;text-decoration:none;margin-right:35px}
.main-nav a.is-active{background:var(--teal-deep);padding:4px 8px;font-weight:700;margin-right:27px}
.user-menu{position:absolute;left:932px;top:49px;display:flex;align-items:center;gap:7px;color:#fff;font-weight:700;font-size:13px}
.header-rule{position:absolute;left:94px;top:82px;width:949px;height:1px;background:rgba(255,255,255,.25)}
.filters{position:absolute;left:94px;top:93px;height:34px;display:flex;gap:4px}
.filter{background:#fff;height:34px;display:flex;align-items:center;justify-content:space-between;
  padding:0 12px 0 14px;font-size:12px;color:#666}
.filter svg{flex:none}

.section-title{position:absolute;left:94px;top:174px;font-size:16px;font-weight:900;color:var(--teal-dark)}
.result-count{position:absolute;right:93px;top:178px;font-size:13px;font-weight:700;color:#555}

.doctor-card{position:absolute;left:94px;width:949px;height:111px;background:var(--card);
  box-shadow:0 1px 2px rgba(0,0,0,.04)}
.doctor-card.is-hover{box-shadow:0 1px 6px rgba(0,0,0,.15)}
.avatar{position:absolute;left:20px;top:16px;width:79px;height:79px;border-radius:50%;
  border:1px solid #e4e4e4;background:radial-gradient(circle at 50% 40%,#cfcfcf 0 30%,#f4f4f4 31%)}
.avatar.photo{background:linear-gradient(160deg,#d7d7d7,#8b98a6 60%,#f1f1f1)}
.doctor-name{position:absolute;left:119px;top:22px;font-size:13px;font-weight:900;color:var(--ink);text-transform:uppercase}
.doctor-name.is-link{color:var(--teal-dark);text-decoration:underline}
.doctor-spec{position:absolute;left:119px;top:49px;font-size:12.5px;color:var(--ink-soft)}
.doctor-addr{position:absolute;left:119px;top:74px;font-size:12.5px;color:var(--ink-soft)}
.rating{position:absolute;right:20px;top:22px;display:flex;align-items:center;gap:12px}
.rating .count{font-size:13px;color:var(--muted)}
.like{position:absolute;right:20px;top:61px;display:flex;align-items:center;gap:14px;font-size:12.5px;color:var(--muted)}
.view-btn{position:absolute;right:113px;top:58px;width:100px;height:34px;background:var(--teal-dark);
  border-bottom:3px solid var(--teal-deep);color:#fff;font-size:12px;font-weight:700;
  display:flex;align-items:center;justify-content:center}

.load-more{position:absolute;left:0;width:1136px;top:828px;text-align:center;font-size:13px;font-weight:700;color:var(--muted);
  display:flex;justify-content:center;align-items:center;gap:10px}

.site-footer{position:absolute;left:0;top:864px;width:1136px;height:272px;background:var(--footer)}
.footer-col{position:absolute;top:42px}
.footer-col h4{font-size:13.5px;font-weight:700;color:#fff;margin-bottom:10px}
.footer-col a{display:block;font-size:12.5px;color:var(--footer-text);text-decoration:none;line-height:22px}
.footer-col a.is-current{color:#fff;font-weight:700}
.social{position:absolute;left:860px;top:46px;width:182px;display:flex;flex-wrap:wrap;justify-content:flex-end;gap:4px 10px;
  font-size:10px;color:#8a8a8a}
.social .is-current{color:#fff}
.logout{position:absolute;left:943px;top:82px;width:98px;height:27px;background:var(--teal-deep);color:#fff;
  font-size:12px;font-weight:700;display:flex;align-items:center;justify-content:center}
.footer-base{position:absolute;left:0;top:1136px;width:1136px;height:64px;background:var(--footer-base)}
.copyright{position:absolute;left:95px;top:24px;font-size:12.5px;color:var(--footer-text)}
.base-brand{position:absolute;right:94px;top:16px;display:flex;align-items:center;gap:6px;color:#ddd;font-weight:900;font-size:22px}
.base-brand .brand-dot{width:10px;height:10px;background:#ddd}
</style>
</head>
<body>
<svg width="0" height="0" style="position:absolute">
  <defs>
    <symbol id="star" viewBox="0 0 24 24"><path d="M12 2l2.9 6.6 7.1.6-5.4 4.7 1.6 7-6.2-3.7-6.2 3.7 1.6-7L2 9.2l7.1-.6z"/></symbol>
    <symbol id="heart" viewBox="0 0 24 24"><path d="M12 21s-7.5-4.6-9.6-9.2C.9 8.3 3 4.5 6.7 4.5c2.2 0 3.7 1.2 5.3 3 1.6-1.8 3.1-3 5.3-3 3.7 0 5.8 3.8 4.3 7.3C19.5 16.4 12 21 12 21z"/></symbol>
    <symbol id="chev" viewBox="0 0 12 8"><path d="M1 1l5 5 5-5" fill="none" stroke="currentColor" stroke-width="1.6"/></symbol>
    <linearGradient id="half"><stop offset="50%" stop-color="#0a8f86"/><stop offset="50%" stop-color="#b5b5b5"/></linearGradient>
  </defs>
</svg>

<header class="site-header">
  <div class="brand"><span class="brand-dot"></span>Curanota</div>
  <nav class="main-nav">
    <a class="is-active">Home</a><a>Write a Review</a><a>Favorite Doctors</a><a>Messages</a><a>Talk</a><a>Events</a>
  </nav>
  <div class="user-menu">
    <svg width="20" height="20" viewBox="0 0 20 20"><circle cx="10" cy="10" r="9" fill="none" stroke="#fff" stroke-width="1.5"/><circle cx="10" cy="8" r="3" fill="#fff"/><path d="M4.5 15.5c1.5-2.5 3.5-3.3 5.5-3.3s4 .8 5.5 3.3" fill="#fff"/></svg>
    Omar Reed
    <svg width="12" height="8" style="color:#fff;margin-left:4px"><use href="#chev"/></svg>
  </div>
  <div class="header-rule"></div>
  <div class="filters">
    <div class="filter" style="width:193px">Search
      <svg width="14" height="14" viewBox="0 0 14 14"><circle cx="6" cy="6" r="4.6" fill="none" stroke="#777" stroke-width="1.3"/><path d="M9.4 9.4l3.4 3.4" stroke="#777" stroke-width="1.3"/></svg></div>
    <div class="filter" style="width:181px">Specialization<svg width="12" height="8" style="color:#888"><use href="#chev"/></svg></div>
    <div class="filter" style="width:181px">Sub-Specialization<svg width="12" height="8" style="color:#888"><use href="#chev"/></svg></div>
    <div class="filter" style="width:140px">Area<svg width="12" height="8" style="color:#0a8f86"><use href="#chev"/></svg></div>
    <div class="filter" style="width:108px">Gender<svg width="12" height="8" style="color:#888"><use href="#chev"/></svg></div>
    <div class="filter" style="width:128px">Rating<svg width="12" height="8" style="color:#888"><use href="#chev"/></svg></div>
  </div>
</header>

<h2 class="section-title">REVIEWED DOCTORS</h2>
<div class="result-count">15,123 Doctors</div>

<article class="doctor-card" style="top:206px">
  <div class="avatar" role="img" aria-label="Default avatar of a male doctor"></div>
  <h3 class="doctor-name">Karim Haddad ( 1 kms away )</h3>
  <p class="doctor-spec">Anesthesiologist</p>
  <p class="doctor-addr">73 Cedar street, Riverside</p>
  <div class="rating">
    <svg width="120" height="20" fill="#0a8f86"><use href="#star" width="20" height="20"/><use href="#star" x="25" width="20" height="20"/><use href="#star" x="50" width="20" height="20"/><use href="#star" x="75" width="20" height="20"/><use href="#star" x="100" width="20" height="20" fill="url(#half)"/></svg>
    <span class="count">( 123 )</span>
  </div>
  <div class="like">LIKE:<svg width="28" height="28" fill="#b5b5b5"><use href="#heart" width="28" height="28"/></svg></div>
</article>

<article class="doctor-card is-hover" style="top:329px">
  <div class="avatar photo" role="img" aria-label="Portrait photo of the doctor"></div>
  <h3 class="doctor-name is-link">Laila Mansour ( 9 kms away )</h3>
  <p class="doctor-spec">Dentist</p>
  <p class="doctor-addr">48 Olive street, Palm District</p>
  <div class="rating">
    <svg width="120" height="20" fill="#0a8f86"><use href="#star" width="20" height="20"/><use href="#star" x="25" width="20" height="20"/><use href="#star" x="50" width="20" height="20"/><use href="#star" x="75" width="20" height="20"/><use href="#star" x="100" width="20" height="20"/></svg>
    <span class="count">( 123 )</span>
  </div>
  <div class="view-btn">VIEW INFO</div>
  <div class="like">LIKE:<svg width="28" height="28" fill="#0a8f86"><use href="#heart" width="28" height="28"/></svg></div>
</article>

<article class="doctor-card" style="top:452px">
  <div class="avatar" role="img" aria-label="Default avatar of a female doctor"></div>
  <h3 class="doctor-name">Salma Nabil ( 8 kms away )</h3>
  <p class="doctor-spec">Pediatrician</p>
  <p class="doctor-addr">122 Maple street, Riverside</p>
  <div class="rating">
    <svg width="120" height="20"><use href="#star" width="20" height="20" fill="#0a8f86"/><use href="#star" x="25" width="20" height="20" fill="#0a8f86"/><use href="#star" x="50" width="20" height="20" fill="#0a8f86"/><use href="#star" x="75" width="20" height="20" fill="#b5b5b5"/><use href="#star" x="100" width="20" height="20" fill="#b5b5b5"/></svg>
    <span class="count">( 123 )</span>
  </div>
  <div class="like">LIKE:<svg width="28" height="28" fill="#b5b5b5"><use href="#heart" width="28" height="28"/></svg></div>
</article>

<article class="doctor-card" style="top:576px">
  <div class="avatar" role="img" aria-label="Default avatar of a female doctor"></div>
  <h3 class="doctor-name">Salma Nabil ( 16 kms away )</h3>
  <p class="doctor-spec">Pediatrician</p>
  <p class="doctor-addr">122 Maple street, Riverside</p>
  <div class="rating">
    <svg width="120" height="20" fill="#0a8f86"><use href="#star" width="20" height="20"/><use href="#star" x="25" width="20" height="20"/><use href="#star" x="50" width="20" height="20"/><use href="#star" x="75" width="20" height="20"/><use href="#star" x="100" width="20" height="20" fill="url(#half)"/></svg>
    <span class="count">( 123 )</span>
  </div>
  <div class="like">LIKE:<svg width="28" height="28" fill="#b5b5b5"><use href="#heart" width="28" height="28"/></svg></div>
</article>

<article class="doctor-card" style="top:698px">
  <div class="avatar" role="img" aria-label="Default avatar of a male doctor"></div>
  <h3 class="doctor-name">Karim Haddad ( 1 kms away )</h3>
  <p class="doctor-spec">Anesthesiologist</p>
  <p class="doctor-addr">73 Cedar street, Riverside</p>
  <div class="rating">
    <svg width="120" height="20" fill="#0a8f86"><use href="#star" width="20" height="20"/><use href="#star" x="25" width="20" height="20"/><use href="#star" x="50" width="20" height="20"/><use href="#star" x="75" width="20" height="20"/><use href="#star" x="100" width="20" height="20" fill="url(#half)"/></svg>
    <span class="count">( 123 )</span>
  </div>
  <div class="like">LIKE:<svg width="28" height="28" fill="#b5b5b5"><use href="#heart" width="28" height="28"/></svg></div>
</article>

<div class="load-more">LOAD MORE <svg width="12" height="8" style="color:#9a9a9a"><use href="#chev"/></svg></div>

<footer class="site-footer">
  <div class="footer-col" style="left:95px"><h4>About</h4><a>About Curanota</a><a>Careers</a><a>Press</a><a>Investor Relations</a><a>Content Guidelines</a></div>
  <div class="footer-col" style="left:292px"><h4>Discover</h4><a>Blog</a><a>Support</a><a>RSS</a></div>
  <div class="footer-col" style="left:489px"><h4>Policies</h4><a>Terms of Service</a><a class="is-current">Privacy Policy</a><a>Ad Privacy Info</a></div>
  <div class="footer-col" style="left:700px"><h4>Languages</h4><a>English</a><a>Arabic</a></div>
  <div class="social"><span>chirpnet</span><span>dotframe</span><span class="is-current">pagecircle</span><span>memoleaf</span><span>ballcraft</span></div>
  <div class="logout">LOGOUT</div>
</footer>
<div class="footer-base">
  <div class="copyright">Copyright © 2004–2015</div>
  <div class="base-brand"><span class="brand-dot"></span>Curanota</div>
</div>
</body>
</html>
```